Business Card Design

My company is a Consulting & Training company (Halvane Consulting and Training, LLC) specializing in Firearms Training, State of Florida Concealed Weapons Permit Course, and Tactical Equipment Consulting.

Industry/Entity Type

Business

Contact Information for Business Card

Dario Holtzmeyer
P.O. Box 417302
Aventura, FL 33917
(786)492-7318

```html
<!DOCTYPE html>
<html lang="en">
<head>
<meta charset="utf-8">
<title>Halvane Consulting &amp; Training – Business Card</title>
<link rel="stylesheet" href="https://fonts.googleapis.com/css2?family=Open+Sans:wght@400;600;700&display=swap">
<style>
  :root {
    --bg: #e4e4e4;
    --card-white: #ffffff;
    --card-dark: #2b2b2b;
    --brand-blue: #3f7ec6;
    --brand-grey: #8e8e8e;
    --ink: #2a2a2a;
    --white: #ffffff;
  }
  * { box-sizing: border-box; margin: 0; padding: 0; }
  html, body {
    width: 1200px; height: 900px; overflow: hidden;
    background: var(--bg);
    font-family: "Open Sans", Arial, sans-serif;
  }
  .stage {
    width: 1200px; height: 900px;
    display: flex; flex-direction: column;
    align-items: center; justify-content: center; gap: 48px;
  }
  .card {
    position: relative; width: 660px; height: 377px; overflow: hidden;
    box-shadow: 0 4px 14px rgba(0,0,0,.18);
  }
  .card--back { background: var(--card-dark); display: flex; align-items: center; justify-content: center; }
  .card--front { background: var(--card-white); }
  .card-art { position: absolute; inset: 0; width: 100%; height: 100%; }

  .back-wordmark {
    color: var(--white); font-weight: 700; font-size: 52px; letter-spacing: 2px;
    display: flex; align-items: center; gap: 16px;
  }
  .back-wordmark .mark-dot { width: 14px; height: 14px; border-radius: 50%; background: var(--white); }

  .holder { position: absolute; left: 64px; top: 24px; }
  .holder-name { color: var(--brand-blue); font-weight: 600; font-size: 24px; line-height: 1.15; }
  .holder-title { color: var(--ink); font-size: 15px; font-weight: 400; }

  .contact {
    position: absolute; left: 40px; top: 168px;
    color: var(--ink); font-size: 14.5px; line-height: 1.4; font-style: normal;
  }
  .contact .address { margin-bottom: 16px; }
  .contact .label { color: var(--brand-blue); display: inline-block; width: 18px; }

  .front-wordmark {
    position: absolute; left: 340px; top: 188px; width: 300px;
    color: var(--brand-blue); font-weight: 700; font-size: 44px; line-height: 1.05;
    text-transform: uppercase; letter-spacing: 2px; white-space: nowrap;
  }
  .front-wordmark .tagline {
    display: block; font-size: 15px; font-weight: 700; letter-spacing: 2.5px; margin-top: 8px;
  }
</style>
</head>
<body>
<main class="stage">
  <section class="card card--back" aria-label="Card back">
    <div class="back-wordmark"><span class="mark-dot"></span>Halvane</div>
  </section>

  <section class="card card--front" aria-label="Card front">
    <svg class="card-art" viewBox="0 0 660 377" aria-hidden="true">
      <polygon points="0,22 48,22 30,62 0,62" fill="var(--brand-blue)"/>
      <polygon points="48,22 58,22 40,62 30,62" fill="var(--brand-grey)"/>
      <polygon points="0,296 318,296 304,322 0,322" fill="var(--brand-grey)"/>
      <polygon points="330,300 660,300 660,352 300,352" fill="var(--brand-blue)"/>
    </svg>

    <header class="holder">
      <h1 class="holder-name">Dario Holtzmeyer</h1>
      <p class="holder-title">Managing Director</p>
    </header>

    <address class="contact">
      <p class="address">P.O. Box 417302<br>Aventura, FL 33917</p>
      <p><span class="label">p:</span>(786)492-7318</p>
      <p><span class="label">f:</span>(786)492-7319</p>
      <p><span class="label">e:</span>info@halvane.example</p>
    </address>

    <div class="front-wordmark">Halvane<span class="tagline">Consulting &amp; Training</span></div>
  </section>
</main>
</body>
</html>
```